Business cards and stationary design

We just completed the design of our new logo and we need to print new business cards and letterhead for our nonprofit. We are looking for a fresh new design that shows off our new logo. On letterhead, we must have a column on the right or left to include our Board of Directors (up to 45 names) (see attachment)

Industry/Entity Type

Non-Profit

Contact Information for Business Card

Standard business card with name, title, Company name, mailing address phone numbers, email address and website. Tagline on back "Bringing the homeless home"

Font styles to use
Sans Serif

Requirements
Must have
• include pertinent information above
• new logo
• fonts compatible with logo
• should use logo colors only
Nice to have
• tag lines

```html
<!DOCTYPE html>
<html lang="en">
<head>
<meta charset="utf-8">
<title>Shelter Bridge Alliance – Business Card</title>
<link rel="stylesheet" href="https://fonts.googleapis.com/css2?family=Bebas+Neue&family=Work+Sans:wght@400;500;600&display=swap">
<style>
  :root {
    --backdrop: #2a2a2a;
    --card: #1c1c1c;
    --card-edge: #262626;
    --gold: #f5b416;
    --teal: #1a8fb0;
    --white: #f2f2f2;
  }
  * { margin: 0; padding: 0; box-sizing: border-box; }
  html, body {
    width: 1200px; height: 900px; overflow: hidden;
    background: var(--backdrop);
    font-family: "Work Sans", sans-serif;
  }
  .canvas {
    position: relative; width: 1200px; height: 900px;
  }
  .card {
    position: absolute; left: 280px;
    width: 640px; height: 366px;
    background: linear-gradient(135deg, var(--card) 0%, var(--card-edge) 100%);
    box-shadow: 0 10px 30px rgba(0,0,0,.45);
  }
  .card-front { top: 60px; }
  .card-back { top: 474px; }

  .brand {
    position: absolute; left: 0; right: 0; top: 50%;
    transform: translateY(-50%);
    display: flex; align-items: center; justify-content: center; gap: 16px;
  }
  .brand-dot {
    width: 34px; height: 34px; border-radius: 50%;
    background: var(--gold);
  }
  .brand-name {
    font-family: "Work Sans", sans-serif;
    font-weight: 600; font-size: 30px; letter-spacing: 3px;
    text-transform: uppercase; color: var(--teal);
  }

  .identity {
    position: absolute; right: 392px; top: 128px;
    text-align: right;
  }
  .person-name {
    font-family: "Bebas Neue", sans-serif;
    font-size: 44px; line-height: 1; color: var(--gold);
    letter-spacing: .5px;
  }
  .person-title {
    font-size: 17px; color: var(--white); margin-top: 4px;
  }
  .divider {
    position: absolute; left: 274px; top: 130px;
    width: 3px; height: 56px; background: var(--gold);
  }
  .contacts {
    position: absolute; left: 300px; top: 124px;
    list-style: none;
  }
  .contacts li {
    display: flex; align-items: center; gap: 10px;
    font-size: 17px; color: var(--white); line-height: 23px;
  }
  .contacts svg { width: 12px; height: 12px; flex: none; }
  .address {
    position: absolute; left: 0; right: 0; top: 268px;
    text-align: center; font-size: 18px; color: var(--white);
  }
</style>
</head>
<body>
<main class="canvas">
  <section class="card card-front">
    <div class="brand">
      <span class="brand-dot"></span>
      <span class="brand-name">Shelter Bridge Alliance</span>
    </div>
  </section>

  <section class="card card-back">
    <div class="identity">
      <h1 class="person-name">Daniel Reyes</h1>
      <p class="person-title">Director</p>
    </div>
    <span class="divider"></span>
    <ul class="contacts">
      <li>
        <svg viewBox="0 0 12 12" aria-hidden="true"><path d="M2.5 1 L4.5 1 L5.2 3.6 L4 4.6 Q5 7 7.4 8 L8.4 6.8 L11 7.5 L11 9.5 Q10.5 11 9 11 Q1 10 1 3 Q1 1.5 2.5 1Z" fill="var(--gold)"/></svg>
        555.014.2290
      </li>
      <li>
        <svg viewBox="0 0 12 12" aria-hidden="true"><rect x="1" y="2.5" width="10" height="7" fill="none" stroke="var(--gold)" stroke-width="1.2"/><path d="M1 2.8 L6 6.5 L11 2.8" fill="none" stroke="var(--gold)" stroke-width="1.2"/></svg>
        info@sbadallas.org
      </li>
      <li>
        <svg viewBox="0 0 12 12" aria-hidden="true"><g fill="none" stroke="var(--gold)" stroke-width="1"><circle cx="6" cy="6" r="5"/><ellipse cx="6" cy="6" rx="2.2" ry="5"/><path d="M1 6 H11 M2 3.5 H10 M2 8.5 H10"/></g></svg>
        www.sbadallas.org
      </li>
    </ul>
    <p class="address">P.O. Box 52018, Dallas, Texas 75201</p>
  </section>
</main>
</body>
</html>
```